Halvicek Law Group, PLLC
Business card and stationery
Professional
Marcus T. Halvicek, Esq.
President
248 Perrin Avenue
Suite 3407
New York, New York 10093
mhalvicek@halviceklawgroup.example
www.halviceklawgroup.example
Using Ivory-colored card stock
There are 2 additional staff members that need cards:
nothing

```html
<!DOCTYPE html>
<html lang="en">
<head>
<meta charset="utf-8">
<title>Halvicek Law Group, PLLC — Stationery</title>
<link rel="stylesheet" href="https://fonts.googleapis.com/css2?family=Lato:wght@400;700&display=swap">
<style>
:root{
  --maroon:#5c1c22;
  --ink:#333333;
  --muted:#777777;
  --paper:#fffef9;
  --backdrop:#d9c29c;
  --line:#9a9a9a;
  --label:#3b2a18;
  --flap:#c9c3b6;
}
*{box-sizing:border-box;margin:0;padding:0}
html,body{width:1200px;height:559px;overflow:hidden}
body{background:var(--backdrop);font-family:"Lato",Arial,sans-serif;color:var(--ink);position:relative}
.sheet,.card,.envelope{position:absolute;background:var(--paper);box-shadow:0 2px 6px rgba(0,0,0,.25)}
.piece-label{position:absolute;font-size:9px;font-weight:700;color:var(--label);text-align:center}

/* Firm name, set as plain text */
.firm-name{font-family:"Lato",Arial,sans-serif;font-weight:700;color:var(--maroon);text-transform:uppercase;letter-spacing:1.5px;line-height:1;white-space:nowrap}
.firm-name-lg{font-size:20px;text-align:center}
.firm-name-sm{font-size:14px}

/* Letter sheets */
.sheet{top:22px;width:365px;height:518px}
.fax-sheet{left:20px}
.letterhead{left:408px}
.sheet .firm-name{margin-top:30px}
.fax-title{position:absolute;top:68px;right:16px;font-size:10px;font-weight:700;color:var(--ink);letter-spacing:1px}
.fax-table{position:absolute;top:82px;left:16px;width:333px;border-collapse:collapse;font-size:8px}
.fax-table td{border:1px solid var(--line);height:20px;padding:0 4px}
.fax-table .key{width:32px}
.checks{position:absolute;top:187px;left:16px;width:333px;display:flex;justify-content:space-between;font-size:7px}
.checks span{display:flex;align-items:center;gap:3px}
.checks i{display:inline-block;width:7px;height:7px;border:1px solid var(--line)}
.signoff{position:absolute;bottom:36px;width:100%;text-align:center;font-size:8px;line-height:1.4}
.signoff strong{color:var(--maroon)}
.sheet-footer{position:absolute;bottom:12px;left:14px;right:14px;border-top:1px solid var(--maroon);padding-top:4px;font-size:5px;color:var(--muted);display:flex;justify-content:space-between}

/* Business card */
.card{left:812px;top:30px;width:348px;height:118px}
.card .firm-name{position:absolute;left:14px;top:18px}
.card-contact{position:absolute;left:14px;top:50px;font-size:6px;line-height:1.45}
.card-contact strong{color:var(--maroon);font-size:7px}
.card-rule{position:absolute;left:200px;right:14px;top:62px;border-top:2px solid var(--maroon)}

/* Envelopes */
.envelope{left:800px;width:372px}
.env-front{top:182px;height:160px}
.env-front .firm-name{position:absolute;left:18px;top:24px}
.env-return{position:absolute;left:18px;top:50px;font-size:6px;line-height:1.45}
.env-band{position:absolute;left:0;right:0;bottom:0;height:14px;background:var(--maroon);color:#fff;font-size:5px;letter-spacing:2px;display:flex;align-items:center;justify-content:center}
.env-back{top:396px;height:140px}
.env-back svg{position:absolute;left:0;top:0}
.env-back .firm-name{position:absolute;left:0;right:0;top:28px;text-align:center}
</style>
</head>
<body>

<div class="piece-label" style="left:20px;top:6px;width:365px">Fax Form</div>
<section class="sheet fax-sheet">
  <div class="firm-name firm-name-lg">Halvicek Law Group, PLLC</div>
  <div class="fax-title">FAX</div>
  <table class="fax-table">
    <tr><td class="key">To:</td><td></td><td class="key">From:</td><td></td></tr>
    <tr><td class="key">Re:</td><td></td><td class="key">Pages:</td><td></td></tr>
    <tr><td class="key">Phone:</td><td></td><td class="key">Date:</td><td></td></tr>
    <tr><td class="key">Fax:</td><td></td><td class="key">CC:</td><td></td></tr>
  </table>
  <div class="checks">
    <span><i></i>Urgent</span><span><i></i>For Review</span><span><i></i>Please Comment</span><span><i></i>Please Reply</span><span><i></i>Please Recycle</span>
  </div>
  <div class="signoff"><strong>Marcus T. Halvicek, Esq.</strong><br>Managing Partner</div>
  <div class="sheet-footer"><span>248 Perrin Avenue, Suite 3407, New York, NY 10093</span><span>T (212) 555-0148 · F (212) 555-0149</span><span>www.halviceklawgroup.example</span></div>
</section>

<div class="piece-label" style="left:408px;top:6px;width:365px">Letterhead</div>
<section class="sheet letterhead">
  <div class="firm-name firm-name-lg">Halvicek Law Group, PLLC</div>
  <div class="signoff"><strong>Marcus T. Halvicek, Esq.</strong><br>Managing Partner</div>
  <div class="sheet-footer"><span>248 Perrin Avenue, Suite 3407, New York, NY 10093</span><span>T (212) 555-0148 · F (212) 555-0149</span><span>www.halviceklawgroup.example</span></div>
</section>

<div class="piece-label" style="left:800px;top:14px;width:372px">Business Card (Front)</div>
<section class="card">
  <div class="firm-name firm-name-sm">Halvicek Law Group, PLLC</div>
  <div class="card-contact">
    <strong>Marcus T. Halvicek, Esq.</strong><br>President<br>
    248 Perrin Avenue, Suite 3407<br>New York, New York 10093<br>
    T (212) 555-0148<br>mhalvicek@halviceklawgroup.example
  </div>
  <div class="card-rule"></div>
</section>

<div class="piece-label" style="left:800px;top:166px;width:372px">Envelope (Front)</div>
<section class="envelope env-front">
  <div class="firm-name firm-name-sm">Halvicek Law Group, PLLC</div>
  <div class="env-return">248 Perrin Avenue, Suite 3407<br>New York, New York 10093</div>
  <div class="env-band">WWW.HALVICEKLAWGROUP.EXAMPLE</div>
</section>

<div class="piece-label" style="left:800px;top:380px;width:372px">Envelope (Back)</div>
<section class="envelope env-back">
  <svg width="372" height="140" viewBox="0 0 372 140" aria-hidden="true">
    <path d="M0 0 L186 100 L372 0" fill="none" stroke="var(--flap)" stroke-width="1"/>
    <path d="M0 140 L150 80 M372 140 L222 80" fill="none" stroke="#dedad0" stroke-width="1"/>
  </svg>
  <div class="firm-name firm-name-sm">Halvicek Law Group, PLLC</div>
</section>

</body>
</html>
```